Corporate PowerPoint design for edtech focused on developing world / emerging markets

I am involved in a edtech startup focused on providing financial literacy for students and young adults in the developing world and emerging markets; currently focus will be on Africa. We are in discussions with the CEO of a bank in S. Africa and would deploy products throughout much of Africa with them. I need a corporate powerpoint that I can use for my customers and for investor presentation. Company name is Tidemark, which is a surfing term; meant to connotate movement and energy.

Reason: meeting with my partners to evaluate designs later this week.

Target Market(s)

target market is two fold - will be selling to execs at banks and telecommunications companies; also need to present to investors.

Industry/Entity Type

Financial

Font styles to use
Sans Serif

Requirements
Must have
• I'd like to have a slide or two that allow me to do columns for things like feature / benefits or just content that doesn't run left to right across the entire powepoint page.
• otherwise, too much color (other than white) uses a ton of ink, so I don't want a full color background e.g. I don't want a blue or green background. I would like to provide some standard corporate info at the bottom - just basics of contact info, url and ability to change them as necessary

```html
<!DOCTYPE html>
<html lang="en">
<head>
<meta charset="utf-8">
<title>Tidemark – Presentation Template</title>
<link rel="stylesheet" href="https://fonts.googleapis.com/css2?family=Barlow+Condensed:wght@500;600&family=Open+Sans:wght@400;700&display=swap">
<style>
  :root {
    --board: #9b9b9b;
    --white: #ffffff;
    --ocean: #136f8e;
    --teal: #17a3a1;
    --teal-pale: #d8eeee;
    --ink: #3a3a3a;
    --graphite: #4b4b4b;
    --stone: #8c8c8c;
    --mist: #b9b9b9;
    --footer: #d5d5d5;
    --head: "Barlow Condensed", "Arial Narrow", sans-serif;
    --body: "Open Sans", Arial, sans-serif;
  }
  * { box-sizing: border-box; margin: 0; padding: 0; }
  html, body { width: 1135px; height: 1200px; overflow: hidden; }
  body { background: var(--board); font-family: var(--body); color: var(--ink); position: relative; }

  .slide { position: absolute; width: 352px; height: 263px; background: var(--white); overflow: hidden; }
  .slide > * { position: absolute; }
  .row-1 { top: 32px; } .row-2 { top: 322px; } .row-3 { top: 612px; } .row-4 { top: 904px; }
  .col-1 { left: 20px; } .col-2 { left: 392px; } .col-3 { left: 763px; }
  .col-a { left: 246px; } .col-b { left: 632px; }

  .heading { font-family: var(--head); font-weight: 600; text-transform: uppercase; color: var(--teal); line-height: 1; letter-spacing: .2px; }
  .rule { height: 1px; background: var(--ink); }
  .rule-white { height: 1px; background: var(--white); }
  .band-ocean { background: var(--ocean); }
  .label { font-weight: 700; color: var(--teal); font-size: 8.5px; text-transform: uppercase; text-align: center; }
  .copy { font-size: 7.6px; line-height: 1.55; text-align: center; color: var(--ink); }
  .photo { background: linear-gradient(135deg, #cfcfcf, #5a5a5a); }

  /* footer */
  .slide-footer { left: 0; right: 0; bottom: 0; height: 18px; background: var(--footer); display: flex; align-items: center; }
  .footer-item { display: flex; align-items: center; gap: 5px; font-size: 6px; color: #8a8a8a; margin-left: 18px; }
  .footer-item:first-child { margin-left: 14px; }
  .footer-item:nth-child(2) { margin-left: 46px; }
  .footer-dot { width: 7px; height: 7px; border-radius: 50%; background: var(--graphite); }
  .footer-mark { margin-left: auto; height: 100%; width: 56px; background: var(--graphite); display: flex; align-items: center; padding-left: 4px; gap: 14px; }
  .footer-mark .mark-circle { width: 13px; height: 13px; border-radius: 50%; background: var(--white); border: 2px solid var(--teal); }
  .footer-mark span { color: var(--white); font-size: 7px; font-weight: 700; }

  /* brand name */
  .brand { display: flex; align-items: center; gap: 5px; font-family: var(--body); font-weight: 700; color: var(--ocean); text-transform: uppercase; }
  .brand-dot { border-radius: 50%; background: var(--ocean); }

  /* title slide */
  .title-top { left: 47px; top: 0; width: 262px; height: 44px; }
  .title-block { left: 47px; top: 162px; width: 262px; height: 101px; background: var(--teal); text-align: center; color: var(--white); padding-top: 22px; }
  .title-block .main { font-family: var(--head); font-weight: 600; font-size: 28px; line-height: 1; }
  .title-block .sub { font-family: var(--head); font-weight: 500; font-size: 18px; margin-top: 3px; }

  /* timeline */
  .timeline-svg { left: 0; top: 0; }
  .milestone { width: 66px; text-align: center; }
  .milestone .time { font-size: 9px; color: var(--ink); }
  .milestone .label { font-size: 6.5px; }
  .milestone .copy { font-size: 5.5px; line-height: 1.4; }

  /* bullets */
  .corner-square { left: 0; top: 0; width: 67px; height: 50px; background: var(--ocean); }
  .bullets { left: 38px; top: 74px; width: 290px; list-style: none; }
  .bullets li { font-size: 9.6px; line-height: 1.33; margin-bottom: 12px; position: relative; padding-left: 12px; }
  .bullets li::before { content: ""; position: absolute; left: 0; top: 4px; width: 4px; height: 4px; border-radius: 50%; background: var(--ocean); }

  /* columns */
  .column { width: 84px; text-align: center; }
  .column .copy { margin-top: 3px; }
  .avatar { width: 60px; height: 60px; border-radius: 50%; background: #7b7b7b; border: 2px solid var(--white); }

  /* chart */
  .legend-item { left: 24px; width: 80px; height: 34px; }
  .legend-item .name { position: absolute; left: 0; top: 2px; width: 52px; text-align: right; font-size: 6.5px; }
  .legend-item .value { position: absolute; left: 0; top: 11px; width: 74px; text-align: right; font-size: 14px; }
  .legend-item .bar { position: absolute; left: 76px; top: 0; width: 5px; height: 32px; }

  /* contact */
  .contact { right: 259px; text-align: right; color: var(--white); font-size: 6.6px; line-height: 1.35; }
  .contact b { display: block; font-size: 7px; }
</style>
</head>
<body>

<!-- Title slide -->
<section class="slide row-1 col-1">
  <div class="title-top band-ocean"></div>
  <div class="rule" style="left:47px;top:51px;width:262px"></div>
  <div class="brand" style="left:128px;top:102px;font-size:14px"><span>Tidemark</span><i class="brand-dot" style="width:12px;height:12px"></i></div>
  <div class="rule" style="left:47px;top:155px;width:262px"></div>
  <div class="title-block"><p class="main">PRESENTATION TITLE</p><p class="sub">SUBTITLE</p></div>
</section>

<!-- Section slide -->
<section class="slide row-1 col-2">
  <div class="band-ocean" style="left:0;top:0;width:352px;height:26px"></div>
  <div class="rule" style="left:88px;top:76px;width:185px"></div>
  <h2 class="heading" style="left:0;top:94px;width:352px;text-align:center;font-size:46px">Section Title</h2>
  <p class="heading" style="left:0;top:149px;width:352px;text-align:center;font-size:19px;font-weight:500">Subtitle</p>
  <div class="rule" style="left:88px;top:181px;width:185px"></div>
  <div class="band-ocean" style="left:0;top:239px;width:352px;height:24px"></div>
</section>

<!-- Timeline slide -->
<section class="slide row-1 col-3">
  <div class="band-ocean" style="left:0;top:0;width:352px;height:92px"></div>
  <h2 class="heading" style="left:0;top:22px;width:352px;text-align:center;font-size:24px;color:var(--white)">Agenda/ Timeline Title</h2>
  <div class="rule-white" style="left:40px;top:50px;width:272px"></div>
  <svg class="timeline-svg" width="352" height="263" viewBox="0 0 352 263" aria-hidden="true">
    <g fill="none" stroke="var(--ink)" stroke-width="1">
      <line x1="82" y1="95" x2="82" y2="135"/><line x1="131" y1="95" x2="131" y2="190"/>
      <line x1="180" y1="95" x2="180" y2="135"/><line x1="229" y1="95" x2="229" y2="190"/>
      <line x1="286" y1="95" x2="286" y2="135"/>
    </g>
    <rect x="40" y="92" width="280" height="6" fill="var(--graphite)"/>
    <polygon points="318,87 330,95 318,103" fill="var(--graphite)"/>
    <circle cx="34" cy="95" r="12" fill="var(--ocean)" stroke="var(--white)" stroke-width="2"/>
    <path d="M34 88 V95 H39" stroke="var(--white)" stroke-width="1.6" fill="none"/>
    <g fill="var(--teal)" stroke="var(--white)" stroke-width="1.5">
      <circle cx="82" cy="95" r="4"/><circle cx="131" cy="95" r="4"/><circle cx="180" cy="95" r="4"/>
      <circle cx="229" cy="95" r="4"/><circle cx="286" cy="95" r="4"/>
    </g>
  </svg>
  <div class="milestone" style="left:49px;top:135px"><p class="time">00.00</p><p class="label">Lorem Ipsum</p><p class="copy">Lorem Ipsum is simply dummy text of the printing and typesetting industry</p></div>
  <div class="milestone" style="left:98px;top:189px"><p class="time">00.00</p><p class="label">Lorem Ipsum</p><p class="copy">Lorem Ipsum is simply dummy text of the printing and typesetting industry</p></div>
  <div class="milestone" style="left:147px;top:135px"><p class="time">00.00</p><p class="label">Lorem Ipsum</p><p class="copy">Lorem Ipsum is simply dummy text of the printing and typesetting industry</p></div>
  <div class="milestone" style="left:196px;top:189px"><p class="time">00.00</p><p class="label">Lorem Ipsum</p><p class="copy">Lorem Ipsum is simply dummy text of the printing and typesetting industry</p></div>
  <div class="milestone" style="left:253px;top:135px"><p class="time">00.00</p><p class="label">Lorem Ipsum</p><p class="copy">Lorem Ipsum is simply dummy text of the printing and typesetting industry</p></div>
  <footer class="slide-footer"><span class="footer-item"><i class="footer-dot"></i>Lorem ipsum dolor it amet</span><span class="footer-item"><i class="footer-dot"></i>Lorem ipsum</span><span class="footer-item"><i class="footer-dot"></i>Lorem ipsum</span><span class="footer-mark"><i class="mark-circle"></i><span>#</span></span></footer>
</section>

<!-- Regular slide -->
<section class="slide row-2 col-1">
  <div class="corner-square"></div>
  <h2 class="heading" style="left:80px;top:24px;font-size:23px">Regular Slide</h2>
  <div class="rule" style="left:80px;top:50px;width:196px"></div>
  <ul class="bullets">
    <li>Lorem Ipsum is simply dummy text of the printing and typesetting industry. Lorem Ipsum has been the industry's standard dummy text ever since the 1500s, when an unknown printer took a galley of type and scrambled it to make a type specimen</li>
    <li>Lorem Ipsum is simply dummy text of the printing and typesetting industry. Lorem Ipsum has been the industry's standard dummy text ever since the 1500s, when an unknown printer took a galley of type and scrambled it to make a type specimen</li>
  </ul>
  <footer class="slide-footer"><span class="footer-item"><i class="footer-dot"></i>Lorem ipsum dolor it amet</span><span class="footer-item"><i class="footer-dot"></i>Lorem ipsum</span><span class="footer-item"><i class="footer-dot"></i>Lorem ipsum</span><span class="footer-mark"><i class="mark-circle"></i><span>#</span></span></footer>
</section>

<!-- Team slide -->
<section class="slide row-2 col-2">
  <h2 class="heading" style="left:0;top:22px;width:352px;text-align:center;font-size:35px">The Team</h2>
  <div class="rule" style="left:110px;top:60px;width:181px"></div>
  <div style="left:0;top:110px;width:352px;height:135px;background:var(--teal-pale)"></div>
  <div class="avatar" style="left:53px;top:80px"></div>
  <div class="avatar" style="left:145px;top:80px"></div>
  <div class="avatar" style="left:234px;top:80px"></div>
  <div class="column" style="left:41px;top:150px"><p class="label">Lorem Ipsum</p><p class="copy">Lorem Ipsum is simply dummy text of the printing and typesetting industry</p></div>
  <div class="column" style="left:133px;top:150px"><p class="label">Lorem Ipsum</p><p class="copy">Lorem Ipsum is simply dummy text of the printing and typesetting industry</p></div>
  <div class="column" style="left:222px;top:150px"><p class="label">Lorem Ipsum</p><p class="copy">Lorem Ipsum is simply dummy text of the printing and typesetting industry</p></div>
  <footer class="slide-footer"><span class="footer-item"><i class="footer-dot"></i>Lorem ipsum dolor it amet</span><span class="footer-item"><i class="footer-dot"></i>Lorem ipsum</span><span class="footer-item"><i class="footer-dot"></i>Lorem ipsum</span><span class="footer-mark"><i class="mark-circle"></i><span>#</span></span></footer>
</section>

<!-- Profile slide -->
<section class="slide row-2 col-3">
  <div class="photo" role="img" aria-label="Portrait of a team member in a dark business suit" style="left:0;top:0;width:141px;height:263px;background:linear-gradient(90deg,#6f6f6f,#bdbdbd 55%,#e8e8e8)"></div>
  <h2 class="heading" style="left:141px;top:13px;width:211px;text-align:center;font-size:29px">Profile Slide</h2>
  <div class="rule" style="left:162px;top:42px;width:164px;background:var(--teal)"></div>
  <p class="heading" style="left:141px;top:45px;width:211px;text-align:center;font-size:17px;font-weight:500">Subtitle</p>
  <div style="left:160px;top:72px;width:176px">
    <p class="copy" style="font-size:7.8px;line-height:1.45">Lorem ipsum is simply dummy text of the printing and typesetting industry. Lorem Ipsum has been the industry's standard dummy text ever since the 1500s, when an unknown printer took a galley of type and scrambled it to make a type specimen</p>
    <p class="copy" style="font-size:7.8px;line-height:1.45;margin-top:9px">Lorem ipsum is simply dummy text of the printing and typesetting industry. Lorem Ipsum has been the industry's standard dummy text ever since the 1500s, when an unknown printer took a galley of type and scrambled it to make a type specimen</p>
  </div>
  <footer class="slide-footer" style="left:141px"><span class="footer-item"><i class="footer-dot"></i>Lorem ipsum dolor it amet</span><span class="footer-item" style="margin-left:22px"><i class="footer-dot"></i>Lorem ipsum</span><span class="footer-item"><i class="footer-dot"></i>Lorem ipsum</span><span class="footer-mark"><i class="mark-circle"></i><span>#</span></span></footer>
</section>

<!-- Chart slide -->
<section class="slide row-3 col-1">
  <div class="corner-square"></div>
  <h2 class="heading" style="left:80px;top:24px;font-size:23px">Chart Slide</h2>
  <div class="rule" style="left:80px;top:50px;width:196px"></div>
  <div class="legend-item" style="top:78px"><span class="name">Lorem Ipsum</span><span class="value">40%</span><i class="bar" style="background:var(--ocean)"></i></div>
  <div class="legend-item" style="top:115px"><span class="name">Lorem Ipsum</span><span class="value">20%</span><i class="bar" style="background:var(--teal)"></i></div>
  <div class="legend-item" style="top:152px"><span class="name">Lorem Ipsum</span><span class="value">20%</span><i class="bar" style="background:var(--mist)"></i></div>
  <div class="legend-item" style="top:189px"><span class="name">Lorem Ipsum</span><span class="value">10%</span><i class="bar" style="background:var(--graphite)"></i></div>
  <svg style="left:141px;top:78px" width="146" height="146" viewBox="0 0 146 146" role="img" aria-label="Donut chart: 40%, 20%, 20%, 10%">
    <g transform="rotate(-90 73 73)" fill="none" stroke-width="36">
      <circle cx="73" cy="73" r="55" stroke="var(--ocean)" stroke-dasharray="153.6 345.6"/>
      <circle cx="73" cy="73" r="55" stroke="var(--teal)" stroke-dasharray="76.8 345.6" stroke-dashoffset="-153.6"/>
      <circle cx="73" cy="73" r="55" stroke="var(--mist)" stroke-dasharray="76.8 345.6" stroke-dashoffset="-230.4"/>
      <circle cx="73" cy="73" r="55" stroke="var(--graphite)" stroke-dasharray="38.4 345.6" stroke-dashoffset="-307.2"/>
    </g>
    <circle cx="73" cy="73" r="36" fill="var(--white)"/>
    <text x="73" y="81" text-anchor="middle" font-family="Barlow Condensed, sans-serif" font-weight="600" font-size="23" fill="var(--ink)">2014</text>
  </svg>
  <footer class="slide-footer"><span class="footer-item"><i class="footer-dot"></i>Lorem ipsum dolor it amet</span><span class="footer-item"><i class="footer-dot"></i>Lorem ipsum</span><span class="footer-item"><i class="footer-dot"></i>Lorem ipsum</span><span class="footer-mark"><i class="mark-circle"></i><span>#</span></span></footer>
</section>

<!-- Single picture slide -->
<section class="slide row-3 col-2">
  <div class="band-ocean" style="left:0;top:125px;width:352px;height:59px"></div>
  <div class="photo" role="img" aria-label="Black and white photo of a hand moving a chess piece" style="left:15px;top:80px;width:166px;height:126px;background:linear-gradient(135deg,#2e2e2e,#a9a9a9 45%,#e2e2e2 60%,#3a3a3a)"></div>
  <h2 class="heading" style="left:193px;top:88px;font-size:22px;color:var(--ink)">Single Picture</h2>
  <p style="left:193px;top:140px;width:150px;font-size:7.8px;line-height:1.4;color:var(--white)"><b>Lorem Ipsum</b> simply dummy text of the printing and typesetting industry.</p>
  <footer class="slide-footer"><span class="footer-item"><i class="footer-dot"></i>Lorem ipsum dolor it amet</span><span class="footer-item"><i class="footer-dot"></i>Lorem ipsum</span><span class="footer-item"><i class="footer-dot"></i>Lorem ipsum</span><span class="footer-mark"><i class="mark-circle"></i><span>#</span></span></footer>
</section>

<!-- Multiple picture slide -->
<section class="slide row-3 col-3">
  <h2 class="heading" style="left:0;top:18px;width:352px;text-align:center;font-size:23px">Multiple Picture</h2>
  <div class="rule" style="left:86px;top:43px;width:181px"></div>
  <div class="band-ocean" style="left:0;top:73px;width:352px;height:56px"></div>
  <div class="photo" role="img" aria-label="Black and white chess pieces on a board" style="left:12px;top:61px;width:101px;height:76px;background:linear-gradient(135deg,#2e2e2e,#b5b5b5 50%,#444)"></div>
  <div class="photo" role="img" aria-label="Black and white chess pieces on a board" style="left:126px;top:61px;width:98px;height:76px;background:linear-gradient(135deg,#2e2e2e,#b5b5b5 50%,#444)"></div>
  <div class="photo" role="img" aria-label="Black and white chess pieces on a board" style="left:238px;top:61px;width:99px;height:76px;background:linear-gradient(135deg,#2e2e2e,#b5b5b5 50%,#444)"></div>
  <div class="column" style="left:21px;top:146px"><p class="label">Lorem Ipsum</p><p class="copy">Lorem Ipsum is simply dummy text of the printing and typesetting industry</p></div>
  <div class="column" style="left:133px;top:146px"><p class="label">Lorem Ipsum</p><p class="copy">Lorem Ipsum is simply dummy text of the printing and typesetting industry</p></div>
  <div class="column" style="left:246px;top:146px"><p class="label">Lorem Ipsum</p><p class="copy">Lorem Ipsum is simply dummy text of the printing and typesetting industry</p></div>
  <footer class="slide-footer"><span class="footer-item"><i class="footer-dot"></i>Lorem ipsum dolor it amet</span><span class="footer-item"><i class="footer-dot"></i>Lorem ipsum</span><span class="footer-item"><i class="footer-dot"></i>Lorem ipsum</span><span class="footer-mark"><i class="mark-circle"></i><span>#</span></span></footer>
</section>

<!-- Break slide -->
<section class="slide row-4 col-a">
  <div role="img" aria-label="Black and white close-up of roasted coffee beans" style="left:0;top:0;width:352px;height:263px;background:linear-gradient(180deg,#2b2b2b,#6d6d6d 20%,#9a9a9a 50%,#6d6d6d 80%,#262626)"></div>
  <div style="left:0;top:55px;width:352px;height:135px;background:rgba(236,236,236,.86)"></div>
  <p class="heading" style="left:0;top:70px;width:352px;text-align:center;font-size:25px">Coffee</p>
  <h2 class="heading" style="left:0;top:95px;width:352px;text-align:center;font-size:38px">Break</h2>
  <div class="rule" style="left:110px;top:137px;width:160px"></div>
  <p style="left:0;top:144px;width:352px;text-align:center;font-size:12px;line-height:1.15;font-weight:700;color:var(--teal)">Lorem Ipsum is simply<br>dummy text of the<br>printing</p>
</section>

<!-- Closing slide -->
<section class="slide row-4 col-b">
  <div class="band-ocean" style="left:0;top:0;width:103px;height:49px"></div>
  <div style="left:0;top:98px;width:103px;height:165px;background:var(--graphite)"></div>
  <div class="brand" style="left:6px;top:66px;font-size:10px;gap:3px"><span>Tidemark</span><i class="brand-dot" style="width:8px;height:8px"></i></div>
  <div class="contact" style="top:103px"><b>Address</b>Lorem Ipsum is<br>simply dummy text of the<br>printing and typesetting</div>
  <div class="contact" style="top:143px"><b>Phone</b>55 014 xxx</div>
  <div class="contact" style="top:165px"><b>Email</b>hello@tidemark.co</div>
  <div role="img" aria-label="Photo of two business people shaking hands" style="left:103px;top:0;width:249px;height:174px;background:radial-gradient(ellipse at 55% 55%,#c9b29a 0,#8f7762 18%,#4a4a4a 30%,#ffffff 52%)"></div>
  <h2 class="heading" style="left:103px;top:193px;width:249px;text-align:center;font-size:33px">Thank You</h2>
  <div class="rule" style="left:137px;top:229px;width:179px"></div>
</section>

</body>
</html>
```